Dential Clinic Business Card

We need a simple elegant business card. 2 sided. First side with our details, and 2nd side with appointment time rows.

Dark background preferred. Will consider monotone design, or colored. Surprise us.

Details:
SIDE1

Maplewood Square Dental

Dr Peter Hollis
BDSc(Adel) FRZPTA

Shop 42, Maplewood Square
7-19 Birch Parade, Elmhurst VIC 3199
Phone: 03 9555 0148
email: info@maplewoodsquaredental.com.au
site: www.maplewoodsquaredental.com.au
_____________________________________
SIDE 2
Appointed Time ________________________
Notes _______________________

Target Market(s)

Dental Patients

Industry/Entity Type

Healthcare

Contact Information for Business Card

SIDE1

Maplewood Square Dental

Dr Peter Hollis
Shop 42, Maplewood Square
Phone: 03 9555 0148
SIDE 2

Font styles to use
Other font styles liked:
• Comfortaa

Requirements
Must have
• Dr Peter Hollis
BDSc(Adel) FRZPTA

Address
Phone
Email
Website
Nice to have
• Simple elegant design with our logo.
Colored logo.
Light text on dark background - Side 1
Light background so can be written on with dark pen - SIde 2
Should not have
• Too many colors

```html
<!DOCTYPE html>
<html lang="en">
<head>
<meta charset="utf-8">
<title>Maplewood Square Dental – Business Card</title>
<link href="https://fonts.googleapis.com/css2?family=Roboto:wght@300;400;500;700&display=swap" rel="stylesheet">
<style>
  :root {
    --blue: #0096d9;
    --green: #7bc043;
    --grey-text: #6d6e71;
    --rule: #c8c8c8;
    --paper: #ffffff;
    --backdrop: #a3a3a3;
  }
  * { margin: 0; padding: 0; box-sizing: border-box; }
  html, body { width: 1200px; height: 1200px; overflow: hidden; }
  body {
    background: var(--backdrop);
    font-family: 'Roboto', Arial, sans-serif;
    position: relative;
  }
  .card {
    position: absolute;
    top: 303px;
    width: 368px;
    height: 594px;
    background: var(--paper);
    overflow: hidden;
  }
  .card--appointments { left: 200px; }
  .card--details { left: 599px; width: 364px; }

  /* Appointment side */
  .top-band {
    position: absolute; left: 0; top: 0; width: 100%; height: 147px;
    background: var(--blue);
  }
  .brand-disc {
    position: absolute; left: 109px; top: 44px;
    width: 150px; height: 150px; border-radius: 50%;
    background: var(--paper);
  }
  .brand-name {
    position: absolute; left: 0; width: 100%;
    text-align: center; color: var(--blue);
    font-weight: 500; font-size: 19px; letter-spacing: 1px;
    text-transform: uppercase; white-space: nowrap;
  }
  .card--appointments .brand-name { top: 198px; }
  .card--details .brand-name { top: 208px; }

  .field {
    position: absolute; left: 35px; width: 298px;
    border-bottom: 1.5px solid var(--rule);
    font-weight: 700; font-size: 17px; padding-bottom: 1px;
  }
  .field--time { color: var(--blue); }
  .field--notes { color: var(--green); }

  .bottom-band {
    position: absolute; left: 0; bottom: 0; width: 100%; height: 52px;
    background: var(--green);
    color: #fff; font-weight: 700; font-size: 16px;
    display: flex; align-items: center; justify-content: center;
    white-space: nowrap;
  }

  /* Details side */
  .center-line {
    position: absolute; left: 0; width: 100%; text-align: center; white-space: nowrap;
  }
  .dentist-name { top: 303px; color: var(--blue); font-weight: 700; font-size: 21px; }
  .qualifications { top: 331px; color: var(--green); font-size: 16px; }
  .icon-row {
    position: absolute; top: 363px; left: 0; width: 100%;
    display: flex; align-items: center; justify-content: center; gap: 4px;
  }
  .icon-row .rule { width: 50px; height: 1.5px; background: #9a9a9a; margin: 0 3px; }
  .icon-box {
    width: 25px; height: 25px; background: var(--blue); border-radius: 2px;
    display: flex; align-items: center; justify-content: center;
  }
  .contact { color: var(--grey-text); font-size: 16px; font-weight: 300; }
  .contact--phone { top: 400px; }
  .contact--email { top: 421px; }
  .contact--web { top: 442px; color: var(--blue); }
  .contact--web .domain { color: var(--green); }
  .divider {
    position: absolute; top: 475px; left: 88px; width: 194px; height: 1.5px;
    background: #b5b5b5;
  }
  .clinic-name { top: 492px; color: var(--blue); font-weight: 700; font-size: 17px; }
  .address { color: var(--grey-text); font-size: 16px; font-weight: 300; }
  .address--line1 { top: 513px; }
  .address--line2 { top: 534px; }
</style>
</head>
<body>

<section class="card card--appointments">
  <div class="top-band"></div>
  <div class="brand-disc"></div>
  <div class="brand-name">Maplewood Square Dental</div>

  <div class="field field--time" style="top:283px">APPOINTED TIME</div>
  <div class="field field--notes" style="top:328px">NOTES</div>
  <div class="field field--time" style="top:412px">APPOINTED TIME</div>
  <div class="field field--notes" style="top:457px">NOTES</div>

  <div class="bottom-band">www.maplewoodsquaredental.com.au</div>
</section>

<section class="card card--details">
  <div class="brand-name">Maplewood Square Dental</div>

  <div class="center-line dentist-name">DR PETER HOLLIS</div>
  <div class="center-line qualifications">BDSc(Adel) FRZPTA</div>

  <div class="icon-row">
    <span class="rule"></span>
    <span class="icon-box">
      <svg width="15" height="15" viewBox="0 0 24 24" aria-hidden="true">
        <path fill="#fff" d="M6.6 10.8a15.1 15.1 0 0 0 6.6 6.6l2.2-2.2a1 1 0 0 1 1-.25 11.4 11.4 0 0 0 3.6.57 1 1 0 0 1 1 1V20a1 1 0 0 1-1 1A17 17 0 0 1 3 4a1 1 0 0 1 1-1h3.5a1 1 0 0 1 1 1c0 1.25.2 2.45.57 3.6a1 1 0 0 1-.25 1z"/>
      </svg>
    </span>
    <span class="icon-box">
      <svg width="16" height="12" viewBox="0 0 16 12" aria-hidden="true">
        <rect x="0.75" y="0.75" width="14.5" height="10.5" fill="none" stroke="#fff" stroke-width="1.5"/>
        <path d="M1 1l7 6 7-6M1 11l5-4.5M15 11l-5-4.5" fill="none" stroke="#fff" stroke-width="1.2"/>
      </svg>
    </span>
    <span class="icon-box">
      <svg width="16" height="16" viewBox="0 0 16 16" aria-hidden="true">
        <circle cx="8" cy="8" r="7" fill="#fff"/>
        <path d="M8 1v14M1 8h14M8 1c-3 3-3 11 0 14M8 1c3 3 3 11 0 14" fill="none" stroke="#0096d9" stroke-width="1"/>
      </svg>
    </span>
    <span class="rule"></span>
  </div>

  <div class="center-line contact contact--phone">03 9555 0148</div>
  <div class="center-line contact contact--email">info@maplewoodsquaredental.com.au</div>
  <div class="center-line contact contact--web">www.<span class="domain">maplewoodsquaredental</span>.com.au</div>

  <div class="divider"></div>

  <div class="center-line clinic-name">MAPLEWOOD SQUARE DENTAL</div>
  <div class="center-line address address--line1">Shop 42, Maplewood Square</div>
  <div class="center-line address address--line2">7-19 Birch Parade, Elmhurst VIC 3199</div>
</section>

</body>
</html>
```